Game, Voice & Dedicated Server Company Needs a Business Card Design

We need a new business card design, centered around our new logo (PSD provided below).

Designs that we do like:
https://pixelmarsh.net/item/corporate-business-card/5382017?s_rank=43 (needs to be made more eye catching)

Our main areas of business are:
- Dedicated Servers
- Game Servers
- Voice Servers
- Mitigation Security Specialists

Industry/Entity Type

Business

Contact Information for Business Card

On the card: (and anything else you would suggest)
- Staff member name
- Staff member position in company
- Staff member phone number
- Staff member email
- Other / Staff member Skype
- Website link

Colors
9bcb3c
abd036

Requirements
Must have
• Design of Card:
• - Green (same green as the logo)
• - Business / Corporate design
• - Something a little different / abstract that shouts premium

```html
<!DOCTYPE html>
<html lang="en">
<head>
<meta charset="utf-8">
<title>Tideway Servers — Business Card</title>
<link rel="stylesheet" href="https://fonts.googleapis.com/css2?family=Open+Sans:ital,wght@0,400;0,600;0,800;1,400&display=swap">
<style>
  :root {
    --green: #8dc63f;
    --ink: #0c0c0c;
    --paper: #ffffff;
    --stage: #e7e5e1;
    --muted: #d9d9d9;
  }
  * { box-sizing: border-box; margin: 0; padding: 0; }
  html, body {
    width: 1200px; height: 987px; overflow: hidden;
    background: var(--stage);
    font-family: "Open Sans", Arial, sans-serif;
  }
  .card {
    position: absolute;
    width: 615px; height: 352px;
    background: var(--ink);
    overflow: hidden;
    box-shadow: 0 3px 10px rgba(0,0,0,.25);
  }
  .card--front { left: 293px; top: 130px; }
  .card--back { left: 292px; top: 505px; }
  .card__bands { position: absolute; inset: 0; width: 100%; height: 100%; }

  .brand {
    position: absolute;
    display: flex; align-items: center; gap: 14px;
    transform: translateX(-50%);
  }
  .brand__square { width: 46px; height: 46px; background: var(--green); }
  .brand__name {
    color: var(--green);
    font-weight: 800;
    font-size: 32px;
    line-height: 1;
    letter-spacing: -0.5px;
    text-transform: uppercase;
  }
  .card--front .brand { left: 310px; top: 85px; }
  .card--back .brand { left: 310px; top: 146px; }

  .contact { position: absolute; left: 30px; top: 231px; list-style: none; }
  .contact li {
    display: flex; align-items: center; gap: 7px;
    height: 23.4px;
    color: var(--paper);
    font-size: 15.5px;
  }
  .contact svg { width: 15px; height: 15px; flex: none; }

  .person { position: absolute; right: 25px; top: 272px; text-align: right; color: var(--paper); }
  .person__name { font-size: 20px; font-weight: 600; line-height: 1.25; }
  .person__role { font-size: 15.5px; font-weight: 600; line-height: 1.5; }

  .services {
    position: absolute; left: 0; right: 0; top: 263px;
    text-align: center; color: var(--paper);
    font-style: italic; font-size: 16px; line-height: 23px;
  }
  .services__dot { color: var(--green); font-style: normal; }
</style>
</head>
<body>
  <section class="card card--front">
    <svg class="card__bands" viewBox="0 0 525 300" preserveAspectRatio="none" aria-hidden="true">
      <polygon points="0,0 525,0 525,40" fill="var(--paper)"/>
      <polygon points="0,150 525,228 525,300 0,300" fill="var(--green)"/>
    </svg>
    <div class="brand">
      <span class="brand__square"></span>
      <span class="brand__name">Tideway<br>Servers</span>
    </div>
    <ul class="contact">
      <li>
        <svg viewBox="0 0 16 16"><path fill="#fff" d="M3 2h3l1.5 3.5-2 1.2a8 8 0 0 0 3.8 3.8l1.2-2L14 10v3a1.5 1.5 0 0 1-1.5 1.5A11 11 0 0 1 1.5 3.5 1.5 1.5 0 0 1 3 2z"/></svg>
        555 014 2290
      </li>
      <li>
        <svg viewBox="0 0 16 16"><rect x="1" y="3.5" width="14" height="9" fill="#fff"/><path d="M1.5 4l6.5 5 6.5-5" fill="none" stroke="var(--green)" stroke-width="1.2"/></svg>
        name@tidewayhost.com
      </li>
      <li>
        <svg viewBox="0 0 16 16"><circle cx="8" cy="8" r="7" fill="#fff"/><path d="M1 8h14M8 1c-3 3.5-3 10.5 0 14M8 1c3 3.5 3 10.5 0 14" fill="none" stroke="var(--green)" stroke-width="1"/></svg>
        www.tidewayhost.com
      </li>
      <li>
        <svg viewBox="0 0 16 16"><circle cx="8" cy="8" r="7" fill="#fff"/></svg>
        tidewayhost.com
      </li>
    </ul>
    <div class="person">
      <p class="person__name">Alex Morgan</p>
      <p class="person__role">CEO/Founder</p>
    </div>
  </section>

  <section class="card card--back">
    <div class="brand">
      <span class="brand__square"></span>
      <span class="brand__name">Tideway<br>Servers</span>
    </div>
    <div class="services">
      <p>Dedicated Servers <span class="services__dot">●</span> Game Servers</p>
      <p>Voice Servers <span class="services__dot">●</span> Business relations</p>
    </div>
  </section>
</body>
</html>
```